Tandi Mentors - Life coaching program for young people

Life coaching program for young people, A 4 triple fold like it to bright and fun with headings on each page
Front page photo of young people in a life coaching program with company logo , inside first The Program 2nd page What is Life Coaching
3rd Page About Your Life Coach
Outside 1st Page Testimonials 2nd outside page contact page 3 page Title page

Target Market(s)

Young People. Parents and Schools

Industry/Entity Type

Life Coaching

Font styles to use
Serif

Colors
0255a3
3276b5
85acd3
edf2f7
cee9f5

Requirements
Must have
• Lots of colour and be fun to look at but professional
Nice to have
• Fun Graphic headings good use of photos
• would like to focus on design then put in the words to fit area put aside for information
Should not have
• too many words

```html
<!DOCTYPE html>
<html lang="en">
<head>
<meta charset="utf-8">
<title>Tandi Mentors – Trifold Brochure</title>
<link rel="stylesheet" href="https://fonts.googleapis.com/css2?family=Noto+Serif:wght@400;700&display=swap">
<style>
  :root {
    --page-bg: #f2f2f2;
    --navy: #23409a;
    --navy-deep: #1f3a8f;
    --red: #d2281e;
    --red-deep: #c21f17;
    --panel-grey: #e4e4e4;
    --ink: #2b2b2b;
    --brand-ink: #3a2b7d;
    --white: #ffffff;
    --sky-top: #3d67b0;
    --sky-mid: #a9c3cf;
    --field: #c9a65a;
  }
  * { box-sizing: border-box; margin: 0; padding: 0; }
  html, body { width: 1200px; height: 866px; overflow: hidden; background: var(--page-bg); }
  body { font-family: "Noto Serif", Georgia, serif; color: var(--ink); }

  .brochure {
    position: absolute; left: 12px; top: 17px;
    width: 1176px; height: 832px;
    display: flex;
    box-shadow: 0 2px 10px rgba(0,0,0,.18);
  }
  .panel { position: relative; width: 392px; height: 832px; overflow: hidden; }

  /* ---------- Testimonials panel ---------- */
  .panel--testimonials { background: var(--navy); color: var(--white); }
  .photo { position: absolute; }
  .photo--group {
    left: 0; top: 0; width: 392px; height: 306px;
    background: linear-gradient(160deg, #8f86c8 0%, #3c5fb0 45%, #24407f 80%, #6d6a62 100%);
  }
  .section-title {
    position: absolute; left: 27px; top: 336px;
    font-size: 31px; font-weight: 700;
  }
  .testimonial { position: absolute; font-size: 13px; font-weight: 700; line-height: 19px; }
  .testimonial__bullet {
    position: absolute; left: -34px; top: 2px;
    width: 14px; height: 14px; border-radius: 50%; background: var(--red);
  }
  .testimonial__quote { text-align: justify; }
  .testimonial__author { text-align: right; font-size: 12px; margin-top: 4px; }
  .testimonial--one { left: 64px; top: 400px; width: 302px; }
  .testimonial--two { left: 64px; top: 493px; width: 302px; }
  .testimonial--three { left: 165px; top: 596px; width: 201px; }
  .photo--coach {
    left: 0; top: 594px; width: 168px; height: 238px;
    background: linear-gradient(180deg, #2f4aa0 0%, #26304f 45%, #15151c 100%);
  }
  .call-button {
    position: absolute; left: 190px; top: 755px; width: 172px; height: 65px;
    background: var(--red); border-radius: 12px; color: var(--white);
    display: flex; align-items: center; gap: 6px; padding-left: 12px;
    font-weight: 700; font-size: 19px; line-height: 28px;
  }

  /* ---------- Contact panel ---------- */
  .panel--contact { background: var(--panel-grey); }
  .photo--meeting {
    left: 0; top: 0; width: 392px; height: 262px;
    background: linear-gradient(100deg, #2b3138 0%, #56606a 30%, #d7dbe0 55%, #eef0f2 100%);
  }
  .intro-block {
    position: absolute; left: 0; top: 262px; width: 392px; height: 203px;
    background: var(--red); color: var(--white);
    text-align: center; font-weight: 700; font-size: 17px; line-height: 24px;
    padding: 56px 24px 0;
  }
  .brand {
    position: absolute; display: flex; align-items: center; gap: 12px;
    color: var(--brand-ink); font-weight: 700;
  }
  .brand__dot { border-radius: 50%; background: var(--red); flex: none; }
  .brand--contact { left: 34px; top: 530px; font-size: 36px; }
  .brand--contact .brand__dot { width: 26px; height: 26px; }
  .divider { position: absolute; left: 34px; top: 608px; width: 324px; height: 2px; background: var(--ink); }
  .contact-list { position: absolute; left: 34px; top: 630px; list-style: none; font-size: 13px; }
  .contact-list li { display: flex; align-items: flex-start; gap: 10px; height: 29px; line-height: 18px; }
  .contact-list li.tall { height: 50px; }
  .contact-list svg { flex: none; margin-top: 2px; }
  .follow { position: absolute; left: 34px; top: 803px; font-size: 13px; }

  /* ---------- Title panel ---------- */
  .panel--title { background: var(--white); }
  .title-band { position: absolute; left: 0; top: 0; width: 392px; height: 31px; background: var(--navy-deep); }
  .brand--title { left: 32px; top: 74px; font-size: 38px; }
  .brand--title .brand__dot { width: 28px; height: 28px; }
  .photo--meadow {
    left: 0; top: 170px; width: 392px; height: 607px;
    background: linear-gradient(180deg, var(--sky-top) 0%, #6f93bf 28%, var(--sky-mid) 55%, #d9d3a8 72%, var(--field) 85%, #a9873f 100%);
  }
  .title-headline {
    position: absolute; left: 0; top: 212px; width: 392px;
    text-align: center; color: rgba(255,255,255,.88);
    font-size: 31px; line-height: 46px;
  }
  .title-headline span { display: block; font-size: 40px; font-weight: 700; margin-top: 4px; }
  .call-bar {
    position: absolute; left: 0; top: 777px; width: 392px; height: 55px;
    background: var(--red-deep); color: var(--white);
    display: flex; align-items: center; gap: 8px; padding-left: 16px;
    font-size: 25px; font-weight: 700;
  }
</style>
</head>
<body>
<main class="brochure">

  <section class="panel panel--testimonials">
    <div class="photo photo--group" role="img" aria-label="Photo of a coach standing with a group of young people holding certificates in a classroom"></div>
    <h2 class="section-title">Testimonials</h2>

    <blockquote class="testimonial testimonial--one">
      <span class="testimonial__bullet"></span>
      <p class="testimonial__quote">“ Lorem Ispum is the dummy text of the Industry Lorem is the lore dummy lorem of the idselt ”</p>
      <p class="testimonial__author">- Lorem Ispum</p>
    </blockquote>
    <blockquote class="testimonial testimonial--two">
      <span class="testimonial__bullet"></span>
      <p class="testimonial__quote">“ Lorem Ispum is the dummy text of the Industry Lorem is the lore dummy lorem of the idselt ”</p>
      <p class="testimonial__author">- Lorem Ispum</p>
    </blockquote>

    <div class="photo photo--coach" role="img" aria-label="Photo of a smiling man in a suit holding an award"></div>
    <blockquote class="testimonial testimonial--three">
      <span class="testimonial__bullet"></span>
      <p class="testimonial__quote">“ Lorem Ispum is the dummy text of the Industry Lorem is the lore dummy lorem of the idselt ”</p>
      <p class="testimonial__author">- Lorem Ispum</p>
    </blockquote>

    <div class="call-button">
      <svg width="22" height="34" viewBox="0 0 22 34" aria-hidden="true"><path d="M6 2 L11 2 L11 9 L8 11 Q7 17 8 23 L11 25 L11 32 L6 32 Q0 17 6 2 Z" fill="#fff"/></svg>
      <span>Call Us Today<br>123 456 7890</span>
    </div>
  </section>

  <section class="panel panel--contact">
    <div class="photo photo--meeting" role="img" aria-label="Photo of a woman with glasses listening during a one-to-one meeting at a laptop"></div>
    <p class="intro-block">Lorem Ispum is the dummy text of the Industry Lorem is the lore dummy lorem of the idselt</p>

    <div class="brand brand--contact"><span class="brand__dot"></span>Tandi Mentors</div>
    <div class="divider"></div>

    <ul class="contact-list">
      <li class="tall">
        <svg width="14" height="16" viewBox="0 0 14 16" aria-hidden="true"><path d="M7 0 A6 6 0 0 1 13 6 C13 10 7 16 7 16 C7 16 1 10 1 6 A6 6 0 0 1 7 0 Z" fill="#222"/><circle cx="7" cy="6" r="2.2" fill="#e4e4e4"/></svg>
        <span>Street name, State Name<br>State Zip Code</span>
      </li>
      <li>
        <svg width="18" height="14" viewBox="0 0 18 14" aria-hidden="true"><rect x="0.5" y="0.5" width="17" height="13" fill="#222"/><path d="M1 1 L9 8 L17 1" stroke="#e4e4e4" fill="none" stroke-width="1.4"/></svg>
        <span>hello@tandimentors.com</span>
      </li>
      <li>
        <svg width="16" height="16" viewBox="0 0 16 16" aria-hidden="true"><g fill="none" stroke="#333" stroke-width="1"><circle cx="8" cy="8" r="7"/><ellipse cx="8" cy="8" rx="3" ry="7"/><path d="M1 8 H15 M2.5 4.5 H13.5 M2.5 11.5 H13.5"/></g></svg>
        <span>www.tandimentors.com</span>
      </li>
      <li>
        <svg width="14" height="18" viewBox="0 0 14 18" aria-hidden="true"><path d="M4 1 L7 1 L7 5 L5 6 Q4.5 9 5 12 L7 13 L7 17 L4 17 Q0 9 4 1 Z" fill="#222"/></svg>
        <span>123 456 7890</span>
      </li>
      <li>
        <svg width="16" height="16" viewBox="0 0 16 16" aria-hidden="true"><rect x="3" y="0" width="9" height="6" fill="#222"/><rect x="0" y="6" width="16" height="8" fill="#222"/><rect x="3" y="8" width="10" height="2" fill="#e4e4e4"/></svg>
        <span>123 456 7890</span>
      </li>
    </ul>
    <p class="follow">Follow us on @tandimentors</p>
  </section>

  <section class="panel panel--title">
    <div class="title-band"></div>
    <div class="brand brand--title"><span class="brand__dot"></span>Tandi Mentors</div>
    <div class="photo photo--meadow" role="img" aria-label="Photo of a young woman with a rainbow umbrella stretching her arms wide in a sunlit meadow"></div>
    <h1 class="title-headline">Lorem Ispum is the<br>dummy text of the<span>Industry</span></h1>
    <div class="call-bar">
      <svg width="20" height="34" viewBox="0 0 22 34" aria-hidden="true"><path d="M6 2 L11 2 L11 9 L8 11 Q7 17 8 23 L11 25 L11 32 L6 32 Q0 17 6 2 Z" fill="#fff"/></svg>
      <span>Call Us Today 123 456 7890</span>
    </div>
  </section>

</main>
</body>
</html>
```